Zielgruppe
Wir sind ein Vertriebsunternehmen, mit dem Ziel die klassische Finanz und den Kryptosektor zu verbinden. Unsere Zielgruppe sind Menschen zwischn 25 - 45 Jahre.
Aufgabenstellung
Wir sind ein Vertriebsunternehmen, mit dem Ziel die klassische Finanz und den Kryptosektor zu verbinden. Unsere Zielgruppe sind Menschen zwischn 25 - 45 Jahre. Wir sind die Communty und Vertrieb der ersten rechtkonformen STO - Plattform ( Plattform für Wertpapiere im Kryptosektor)
Diese Projekt ist Teil eines Paketes, wir bitten nur Designer mit zu machen die alle benötigten Unterlagen designen können.
Online-Marketing Material
2 Vorlagen Social Media - (Einladung/Event, Sprüche/Information)
Banner
Präsentationsvorlagen - min unterschiedliche 8 Vorlagenseiten /Layouts.
Landingpage Layout f. Funnelsite für Webinaranmeldung mit Platz für Formular
Newsletter Layoutvorlage
Vorlage Infografik
Broschüre / E - Book Designe
Es werden nur Vorlagen benötigt mit 'LoremSum Texten' und Musterbildern. Wir möchten von allen Vorlagen die Originaldatei, uns stehen folgende Grafikprogramme zur Verfügung:
Adobe Photoshop
Adobe Illustrator
Canva
Unsere Akt. Designe (Designe Alt) gefällt uns von der Idee, dennoch wünschen wir es uns moderner und edler mit ein wenig 'spaceig'. - Eben die Vereinigung von Kryptowelt und klassischer Finanz.
Schriftart: Poppins
Farben lt. Logo

```html
<!DOCTYPE html>
<html lang="de">
<head>
<meta charset="utf-8">
<title>Infografik – Vorlage</title>
<link href="https://fonts.googleapis.com/css2?family=Poppins:wght@500;700;800&display=swap" rel="stylesheet">
<style>
  :root {
    --navy: #0d2b5e;
    --ink: #1a1a22;
    --blue-deep: #1c4c8a;
    --blue-mid: #2a62a0;
    --blue-soft: #4aa6dc;
    --blue-light: #62c4ee;
    --paper: #ffffff;
    --backdrop: #ffffff;
  }
  * { box-sizing: border-box; margin: 0; padding: 0; }
  html, body { width: 1200px; height: 848px; overflow: hidden; background: var(--backdrop); }
  body { font-family: "Poppins", sans-serif; color: var(--ink); position: relative; }

  .sheet {
    position: absolute; left: 20px; top: 13px; width: 1161px; height: 823px;
    background: var(--paper);
    box-shadow: 0 0 9px rgba(0,0,0,.35);
  }
  .connectors { position: absolute; left: 0; top: 0; width: 1200px; height: 848px; }
  .connectors polyline { fill: none; stroke-width: 3; stroke-linecap: round; stroke-linejoin: round; }

  .hub {
    position: absolute; left: 472px; top: 278px; width: 256px; height: 256px;
    border-radius: 50%; background: var(--paper);
    box-shadow: 0 2px 8px rgba(0,0,0,.35);
    display: flex; align-items: center; justify-content: center;
  }
  .hub-title { font-weight: 800; font-size: 31px; letter-spacing: .3px; color: var(--ink); margin-top: -6px; }

  .node {
    position: absolute; width: 102px; height: 102px; border-radius: 50%;
    background: var(--paper); box-shadow: 0 2px 7px rgba(0,0,0,.35);
    display: flex; align-items: center; justify-content: center;
  }
  .node svg { width: 54px; height: 74px; }
  .node svg * { fill: none; stroke: #000; stroke-width: 4.5; }

  .entry { position: absolute; width: 162px; }
  .entry-title { font-weight: 800; font-size: 16.5px; color: var(--navy); line-height: 1; white-space: nowrap; }
  .entry-rule { height: 3px; border-radius: 2px; margin-top: 6px; }
  .entry-text {
    font-weight: 500; font-size: 11.8px; line-height: 14.3px; color: var(--ink);
    width: 138px;
  }
  .entry-text span {
    display: block; white-space: nowrap;
    text-align: justify; text-align-last: justify;
  }
  .entry.left .entry-rule { width: 149px; margin-left: 2px; }
  .entry.right .entry-rule { width: 161px; }

  .brand {
    position: absolute; left: 500px; top: 750px; width: 200px;
    display: flex; align-items: center; justify-content: center; gap: 7px;
  }
  .brand-dot { width: 14px; height: 14px; border-radius: 50%; background: var(--blue-mid); }
  .brand-name { font-weight: 700; font-size: 19px; color: var(--blue-mid); }
</style>
</head>
<body>
  <div class="sheet"></div>

  <svg class="connectors" viewBox="0 0 1200 848" aria-hidden="true">
    <polyline points="370,242 487,241 515,279" stroke="#1c4c8a"/>
    <polyline points="372,406 450,406" stroke="#2a5e95"/>
    <polyline points="371,571 487,571 514,534" stroke="#5fb6e2"/>
    <polyline points="686,281 715,242 831,243" stroke="#4fa3d6"/>
    <polyline points="752,407 832,407" stroke="#1f538f"/>
    <polyline points="686,532 715,571 832,570" stroke="#1d4f8c"/>
  </svg>

  <div class="hub"><h1 class="hub-title">LOREM IPSUM</h1></div>

  <svg width="0" height="0" style="position:absolute">
    <symbol id="coin-lock" viewBox="0 0 54 74">
      <path d="M12 29 V20 a15 15 0 0 1 30 0 V29"/>
      <rect x="3" y="29" width="48" height="41" rx="8"/>
      <circle cx="27" cy="49.5" r="14"/>
      <circle cx="27" cy="49.5" r="7"/>
    </symbol>
  </svg>

  <div class="node" style="left:249px;top:193px"><svg><use href="#coin-lock"/></svg></div>
  <div class="node" style="left:249px;top:356px"><svg><use href="#coin-lock"/></svg></div>
  <div class="node" style="left:249px;top:519px"><svg><use href="#coin-lock"/></svg></div>
  <div class="node" style="left:849px;top:193px"><svg><use href="#coin-lock"/></svg></div>
  <div class="node" style="left:849px;top:356px"><svg><use href="#coin-lock"/></svg></div>
  <div class="node" style="left:849px;top:519px"><svg><use href="#coin-lock"/></svg></div>

  <div class="entry left" style="left:100px;top:209px">
    <h2 class="entry-title">LOREM IPSUM</h2>
    <div class="entry-rule" style="background:#0d2f66"></div>
    <p class="entry-text" style="margin-top:11px"><span>Lorem ipsum dolor</span><span>sit amet, consectetur</span><span>adipiscing elit, sed</span><span>do eiusmod tempor</span><span>incididunt ut labore</span><span>et dolore magna</span><span>aliqua. Quis ipsum</span><span>suspendisse ultrices</span></p>
  </div>
  <div class="entry left" style="left:100px;top:376px">
    <h2 class="entry-title">LOREM IPSUM</h2>
    <div class="entry-rule" style="background:#3c8cc8"></div>
    <p class="entry-text" style="margin-top:8px"><span>Lorem ipsum dolor</span><span>sit amet, consectetur</span><span>adipiscing elit, sed</span><span>do eiusmod tempor</span><span>incididunt ut labore</span><span>et dolore magna</span><span>aliqua. Quis ipsum</span><span>suspendisse ultrices</span></p>
  </div>
  <div class="entry left" style="left:100px;top:538px">
    <h2 class="entry-title">LOREM IPSUM</h2>
    <div class="entry-rule" style="background:#5ec3ea"></div>
    <p class="entry-text" style="margin-top:11px"><span>Lorem ipsum dolor</span><span>sit amet, consectetur</span><span>adipiscing elit, sed</span><span>do eiusmod tempor</span><span>incididunt ut labore</span><span>et dolore magna</span><span>aliqua. Quis ipsum</span><span>suspendisse ultrices</span></p>
  </div>

  <div class="entry right" style="left:951px;top:208px">
    <h2 class="entry-title">LOREM IPSUM</h2>
    <div class="entry-rule" style="background:#6fd0f2"></div>
    <p class="entry-text" style="margin-top:11px"><span>Lorem ipsum dolor</span><span>sit amet, consectetur</span><span>adipiscing elit, sed</span><span>do eiusmod tempor</span><span>incididunt ut labore</span><span>et dolore magna</span><span>aliqua. Quis ipsum</span><span>suspendisse ultrices</span></p>
  </div>
  <div class="entry right" style="left:951px;top:373px">
    <h2 class="entry-title">LOREM IPSUM</h2>
    <div class="entry-rule" style="background:#4aa8dc"></div>
    <p class="entry-text" style="margin-top:17px"><span>Lorem ipsum dolor</span><span>sit amet, consectetur</span><span>adipiscing elit, sed</span><span>do eiusmod tempor</span><span>incididunt ut labore</span><span>et dolore magna</span><span>aliqua. Quis ipsum</span><span>suspendisse ultrices</span></p>
  </div>
  <div class="entry right" style="left:951px;top:538px">
    <h2 class="entry-title">LOREM IPSUM</h2>
    <div class="entry-rule" style="background:#17407a"></div>
    <p class="entry-text" style="margin-top:16px"><span>Lorem ipsum dolor</span><span>sit amet, consectetur</span><span>adipiscing elit, sed</span><span>do eiusmod tempor</span><span>incididunt ut labore</span><span>et dolore magna</span><span>aliqua. Quis ipsum</span><span>suspendisse ultrices</span></p>
  </div>

  <div class="brand">
    <span class="brand-dot"></span>
    <span class="brand-name">SilberKranich</span>
  </div>
</body>
</html>
```